Brand Identity Stationary Package

Hello I'm looking for a full branding package for my Property Management Company. I have a logo but looking to have the following
Business Card
Email signature
Facebook cover photo
Letterhead (word.doc)
#10 Envelope
Pocket Folder - link to 9x12 pocket folder design specs https://www.quillpress.ca/marketing-materials/presentation-folders
would like everything to match and be brand identifiable. The company looks after residential properties/apartments and some commercial properties. Attached is a zip of the files.
For Business Card
Name: Morgan Tillsey
Position: Operations Manager
Number: 1 (506) 384-2971
Email: Morgan@harbrook.ca
Website: Harbrook.ca
Industry/Entity Type
Property Management

```html
<!DOCTYPE html>
<html lang="en">
<head>
<meta charset="UTF-8">
<title>Harbrook Letterhead</title>
<link href="https://fonts.googleapis.com/css2?family=Montserrat:wght@400;500;700&display=swap" rel="stylesheet">
<style>
  :root {
    --brand-green: #84ad3b;
    --ink: #1a1a1a;
    --paper: #ffffff;
    --backdrop: #e9e9e9;
  }
  * { margin: 0; padding: 0; box-sizing: border-box; }
  html, body {
    width: 1200px;
    height: 960px;
    overflow: hidden;
    background: var(--backdrop);
    font-family: "Montserrat", Arial, sans-serif;
  }
  .letterhead {
    position: absolute;
    left: 282px;
    top: 30px;
    width: 636px;
    height: 900px;
    background: var(--paper);
    box-shadow: 0 4px 18px rgba(0,0,0,0.12);
    overflow: hidden;
  }
  .brand {
    position: absolute;
    left: 44px;
    top: 150px;
    display: flex;
    align-items: center;
    gap: 10px;
  }
  .brand-mark {
    width: 16px;
    height: 16px;
    background: var(--brand-green);
  }
  .brand-name {
    font-weight: 700;
    font-size: 30px;
    letter-spacing: 2px;
    color: var(--ink);
    line-height: 1;
  }
  .contact {
    position: absolute;
    left: 392px;
    top: 40px;
    padding-left: 14px;
    border-left: 1.5px solid var(--brand-green);
    color: var(--ink);
    font-size: 11.5px;
    line-height: 1.45;
  }
  .contact-name {
    color: var(--brand-green);
    font-weight: 700;
    text-transform: uppercase;
    font-size: 12px;
  }
  .contact-role { margin-bottom: 3px; }
  .contact-row {
    display: flex;
    align-items: center;
    gap: 7px;
  }
  .contact-row svg { width: 10px; height: 10px; flex: none; }
  .wave {
    position: absolute;
    left: 0;
    bottom: 0;
    width: 636px;
    height: 180px;
  }
</style>
</head>
<body>
  <main class="letterhead">
    <div class="brand">
      <span class="brand-name">HARBROOK</span>
      <span class="brand-mark"></span>
    </div>

    <address class="contact" style="font-style:normal">
      <div class="contact-name">Morgan Tillsey</div>
      <div class="contact-role">Operations Manager</div>
      <div class="contact-row">
        <svg viewBox="0 0 10 10"><path d="M2 1l2 0 1 2.5-1.3 1a5 5 0 0 0 2.8 2.8l1-1.3L10 7v2a1 1 0 0 1-1 1A9 9 0 0 1 0 2a1 1 0 0 1 1-1z" fill="var(--brand-green)"/></svg>
        <span>1 (506) 384-2971</span>
      </div>
      <div class="contact-row">
        <svg viewBox="0 0 10 10"><rect x="0" y="2" width="10" height="6.5" fill="var(--brand-green)"/><path d="M0 2.3l5 3.3 5-3.3" stroke="#fff" stroke-width="0.9" fill="none"/></svg>
        <span>Morgan@harbrook.ca</span>
      </div>
      <div class="contact-row">
        <svg viewBox="0 0 10 10"><circle cx="5" cy="5" r="4.6" fill="var(--brand-green)"/><path d="M0.5 5h9M5 0.5c-2.4 2.6-2.4 6.4 0 9M5 0.5c2.4 2.6 2.4 6.4 0 9" stroke="#fff" stroke-width="0.7" fill="none"/></svg>
        <span>Harbrook.ca</span>
      </div>
    </address>

    <svg class="wave" viewBox="0 0 636 180" preserveAspectRatio="none">
      <path d="M14 180 C24 120 80 108 190 100 C330 90 470 96 560 60 C600 44 625 26 636 14 L636 180 Z" fill="var(--brand-green)"/>
      <path d="M2 180 C10 110 70 94 185 86 C325 76 462 82 552 46 C592 30 616 12 626 0"
            stroke="var(--ink)" stroke-width="4.5" fill="none"/>
    </svg>
  </main>
</body>
</html>
```